Frizzle! A stand up comedy show- poster and other graphics required

We require a design for a new late night comedy show called 'Frizzle!' which will appear at festivals and feature a variety of stand up acts as well as inviting the audience to heckle the comedians on stage. The final design should be bold and stand out loudly, to fit the late night raucous nature of the show.
We need a poster image as well as smaller images for program guides and websites. This is going to be the kind of show people talk about so needs a poster to match!!

Target Market(s)

Comedy fans, 20-40 year olds, late night adult audience

Requirements
Nice to have
• We don't really have any clear design in mind so happy to leave it to interpretation but possible ideas would be: a silhouette of a head shouting / a mic is always an iconic image / the simple outline of an audience with obscenities (@*!& etc) coming out of them / perhaps a mic having fallen over because of a stand-up running off stage!
• But again these are vague ideas. Please message for more info about the show if it helps
Should not have
• Not too busy

```html
<!DOCTYPE html>
<html lang="en">
<head>
<meta charset="utf-8">
<title>Frizzle! — Late Night Comedy</title>
<link rel="stylesheet" href="https://fonts.googleapis.com/css2?family=Alfa+Slab+One&family=Damion&family=Oswald:wght@700&display=block">
<style>
  :root {
    --teal-deep: #135e6a;
    --teal: #1f6f7a;
    --curtain: #c3282c;
    --curtain-dark: #7e1518;
    --curtain-light: #e0474a;
    --title: #ffffff;
    --title-shadow: #5a1214;
    --script: #162f6b;
    --label: #ffffff;
    --sparkle: rgba(214, 233, 236, 0.85);
    --mic-light: #cfc9c4;
    --mic-mid: #8e8a87;
    --mic-dark: #2f3a3e;
  }
  html, body {
    margin: 0;
    padding: 0;
    overflow: hidden;
    background: #ffffff;
  }
  .poster {
    position: relative;
    width: 905px;
    height: 1200px;
    overflow: hidden;
    background:
      radial-gradient(ellipse 300px 520px at 50% 38%, rgba(185, 210, 214, 0.75) 0%, rgba(120, 170, 178, 0.35) 55%, rgba(31, 111, 122, 0) 100%),
      linear-gradient(180deg, var(--teal) 0%, var(--teal-deep) 100%);
  }
  .curtain {
    position: absolute;
    top: 0;
    left: 0;
    width: 905px;
    height: 290px;
  }
  .show-title {
    position: absolute;
    top: 58px;
    left: 0;
    width: 905px;
    margin: 0;
    text-align: center;
    font-family: "Alfa Slab One", Georgia, serif;
    font-weight: 400;
    font-size: 112px;
    line-height: 1;
    letter-spacing: 16px;
    color: var(--title);
    text-shadow: 4px 5px 0 var(--title-shadow);
  }
  .tagline {
    position: absolute;
    top: 238px;
    left: 0;
    width: 905px;
    margin: 0;
    text-align: center;
    font-family: "Damion", "Brush Script MT", cursive;
    font-weight: 400;
    font-size: 92px;
    line-height: 1.1;
    color: var(--script);
  }
  .sparkles {
    position: absolute;
    top: 440px;
    left: 0;
    width: 905px;
    height: 460px;
  }
  .microphone {
    position: absolute;
    top: 446px;
    left: 262px;
    width: 283px;
    height: 754px;
    border-radius: 90px 90px 0 0;
    background: linear-gradient(180deg, var(--mic-light) 0%, var(--mic-mid) 45%, var(--mic-dark) 100%);
  }
  .event-label {
    position: absolute;
    top: 950px;
    margin: 0;
    font-family: "Oswald", "Arial Narrow", sans-serif;
    font-weight: 700;
    font-size: 52px;
    line-height: 1.2;
    color: var(--label);
  }
  .event-label--time { left: 55px; }
  .event-label--venue { left: 551px; }
</style>
</head>
<body>
<main class="poster">
  <svg class="curtain" viewBox="0 0 905 290" role="img" aria-label="Red theatre stage curtain swags across the top">
    <defs>
      <linearGradient id="curtainFill" x1="0" y1="0" x2="0" y2="1">
        <stop offset="0" stop-color="var(--curtain-dark)"/>
        <stop offset="0.55" stop-color="var(--curtain)"/>
        <stop offset="1" stop-color="var(--curtain-light)"/>
      </linearGradient>
    </defs>
    <path fill="url(#curtainFill)" d="M0 0 H905 V290 C860 250 780 215 690 205 C640 200 610 235 600 245 C560 210 500 195 452 200 C400 195 340 210 300 245 C290 235 260 200 210 205 C120 215 45 250 0 290 Z"/>
  </svg>

  <h1 class="show-title">'FRIZZLE!'</h1>
  <p class="tagline">late night comedy</p>

  <svg class="sparkles" viewBox="0 0 905 460" aria-hidden="true">
    <g fill="var(--sparkle)">
      <path d="M88 5 Q92 21 108 25 Q92 29 88 45 Q84 29 68 25 Q84 21 88 5Z"/>
      <path d="M248 52 Q253 75 278 80 Q253 85 248 108 Q243 85 218 80 Q243 75 248 52Z"/>
      <path d="M195 112 Q202 150 245 157 Q202 164 195 202 Q188 164 145 157 Q188 150 195 112Z"/>
      <path d="M178 240 Q183 258 202 262 Q183 266 178 284 Q173 266 154 262 Q173 258 178 240Z"/>
      <path d="M248 395 Q252 410 266 413 Q252 416 248 431 Q244 416 230 413 Q244 410 248 395Z"/>
      <path d="M678 60 Q682 78 700 82 Q682 86 678 104 Q674 86 656 82 Q674 78 678 60Z"/>
      <path d="M635 150 Q640 170 662 174 Q640 178 635 198 Q630 178 608 174 Q630 170 635 150Z"/>
      <path d="M648 240 Q656 285 700 292 Q656 299 648 345 Q640 299 596 292 Q640 285 648 240Z"/>
    </g>
  </svg>

  <div class="microphone" role="img" aria-label="Photo of a vintage chrome stage microphone on a stand"></div>

  <p class="event-label event-label--time">TIME :</p>
  <p class="event-label event-label--venue">VENUE :</p>
</main>
</body>
</html>
```